New Business Card Design Project

I have a logo I would like to use on the business card. I want something that will stand out and that will be remembered.

Target Market(s)

People who collect gems, minerals and crystals.

Contact Information for Business Card

email - mkthestonefalcon@vendrollo.com
phone # 917-406-2581

Font styles to use
Serif
Sans Serif
Decorative

Colors

Designer to choose colors to be used in the design.

Requirements
Must have
• The logo...two to choose from.
Nice to have
• An eye catching and memorable way to draw in people who collect gems minerals and crystals.

```html
<!DOCTYPE html>
<html lang="en">
<head>
<meta charset="utf-8">
<title>The Stone Falcon – Business Card</title>
<link href="https://fonts.googleapis.com/css2?family=Archivo+Black&family=Roboto:wght@400&display=swap" rel="stylesheet">
<style>
  :root {
    --page-bg: #e9e7e3;
    --stone-light: #f4f4f3;
    --stone-mid: #e3e2e0;
    --royal-blue: #1d12c9;
    --royal-blue-light: #4a44e0;
    --mascot-dark: #151515;
    --mascot-mid: #5a5a5a;
    --ink: #111111;
    --white: #ffffff;
  }
  html, body {
    margin: 0;
    width: 1200px;
    height: 950px;
    overflow: hidden;
    background: var(--page-bg);
  }
  .card {
    position: absolute;
    left: 75px;
    top: 175px;
    width: 1050px;
    height: 600px;
    border-radius: 36px;
    overflow: hidden;
    background: radial-gradient(circle at 70% 30%, var(--stone-light), var(--stone-mid));
    box-shadow: 0 12px 30px rgba(0,0,0,0.18);
  }
  .card-band {
    position: absolute;
    inset: 0;
    width: 100%;
    height: 100%;
  }
  .mascot-area {
    position: absolute;
    left: 70px;
    top: 70px;
    width: 380px;
    height: 470px;
    border-radius: 48px;
    background: radial-gradient(ellipse at 45% 40%, var(--mascot-mid), var(--mascot-dark) 75%);
    opacity: 0.9;
  }
  .contact-block {
    position: absolute;
    right: 90px;
    top: 66px;
    text-align: right;
  }
  .holder-name {
    margin: 0;
    font-family: "Archivo Black", sans-serif;
    font-size: 46px;
    letter-spacing: 1px;
    color: var(--ink);
    text-transform: uppercase;
    line-height: 1;
  }
  .holder-title {
    margin: 8px 0 24px;
    font-family: "Roboto", sans-serif;
    font-size: 24px;
    color: var(--royal-blue);
    text-transform: uppercase;
  }
  .contact-line {
    margin: 4px 0;
    font-family: "Roboto", sans-serif;
    font-size: 23px;
    color: var(--ink);
  }
  .brand-lockup {
    position: absolute;
    right: 90px;
    bottom: 66px;
    text-align: right;
  }
  .brand-name {
    margin: 0;
    font-family: "Archivo Black", sans-serif;
    font-size: 64px;
    color: var(--ink);
    text-transform: uppercase;
    line-height: 1.02;
  }
  .brand-tagline {
    margin: 14px 0 0;
    font-family: "Archivo Black", sans-serif;
    font-size: 20px;
    letter-spacing: 4px;
    color: var(--royal-blue);
    text-transform: uppercase;
  }
</style>
</head>
<body>
  <div class="card">
    <svg class="card-band" viewBox="0 0 1050 600" aria-hidden="true">
      <defs>
        <linearGradient id="bandBlue" x1="0" y1="0" x2="1" y2="1">
          <stop offset="0" stop-color="#1d12c9"/>
          <stop offset="1" stop-color="#4a44e0"/>
        </linearGradient>
      </defs>
      <polygon points="0,120 0,600 470,600" fill="url(#bandBlue)"/>
      <line x1="0" y1="120" x2="470" y2="600" stroke="#ffffff" stroke-width="6"/>
    </svg>

    <div class="mascot-area" role="img" aria-label="Brand mascot logo holding crystals and a pickaxe"></div>

    <div class="contact-block">
      <p class="holder-name">Dana Marsh</p>
      <p class="holder-title">CEO/Founder</p>
      <p class="contact-line">917-406-2581</p>
      <p class="contact-line">mkthestonefalcon@vendrollo.com</p>
      <p class="contact-line">www.thestonefalcon.com</p>
    </div>

    <div class="brand-lockup">
      <p class="brand-name">The Stone<br>Falcon</p>
      <p class="brand-tagline">Gems · Minerals · Crystals</p>
    </div>
  </div>
</body>
</html>
```